About us:
Looking for eye catching cards for our 4D/HD Ultrasound Studio.

Description:
We are the premier 4D/HD Ultrasound studio in Pensacola/Pace as well as the greater panhandle area. We are a 4D/HD Ultrasound Studio in Pace, Florida, just a few minutes north of Pensacola. We offer 4D/HD imagining an early gender determination, 8 weeks by blood test and 14 weeks by ultrasound. We utilize the latest in 4D/HD technology to render beautiful images and memories that will last a lifetime.

At 4D Tiny Glimpse of Pace, we give a whole new meaning to ultrasounds. We utilize the most up-to-date 4D/HD ultrasound imaging, so we can provide clear, amazing images of your unborn baby to life. Will she have your nose or her Daddy's smile? Book your appointment today for an unforgettable experience. We also offer heartbeat animals.

Phone: 8505550147
www.4dtinyglimpse.example
address: 2716 -B HWY 38
Pace, FL 32590

Target Market(s)

Pregnant women

Requirements
Should not have
• Ultrasound training

```html
<!DOCTYPE html>
<html lang="en">
<head>
<meta charset="utf-8">
<title>4D Tiny Glimpse of Pace – Rack Cards</title>
<link rel="stylesheet" href="https://fonts.googleapis.com/css2?family=Roboto+Condensed:wght@400;700&family=Source+Sans+3:wght@400&display=swap">
<style>
  :root {
    --teal: #23727a;
    --teal-dark: #1b5c63;
    --ink: #5a5a5a;
    --grey-heading: #6b6b6b;
    --pink: #e5475f;
    --paper: #ffffff;
    --backdrop: #2e2e2e;
    --baby-light: #f2b49a;
    --baby-dark: #8e2a1c;
  }
  * { box-sizing: border-box; margin: 0; padding: 0; }
  html, body { width: 1111px; height: 1200px; overflow: hidden; }
  body { background: var(--backdrop); position: relative; font-family: "Source Sans 3", sans-serif; }

  .card { position: absolute; top: 108px; width: 438px; height: 985px; background: var(--paper); overflow: hidden; box-shadow: 0 8px 18px rgba(0,0,0,.45); }
  .card--front { left: 84px; }
  .card--back { left: 590px; }
  .card__art { position: absolute; inset: 0; }

  .heading { font-family: "Roboto Condensed", sans-serif; font-weight: 700; color: var(--teal); line-height: 1; position: absolute; white-space: nowrap; }

  /* front */
  .brand-name { position: absolute; left: 280px; top: 268px; width: 124px; text-align: center; font-family: "Roboto Condensed", sans-serif; font-weight: 400; font-size: 17px; line-height: 1.15; color: var(--teal); }
  .partner { position: absolute; left: 236px; top: 410px; display: flex; align-items: center; gap: 8px; }
  .partner__name { font-family: "Source Sans 3", sans-serif; font-size: 22px; line-height: 1.05; color: var(--pink); }
  .partner__dot { width: 32px; height: 32px; border-radius: 50%; background: var(--pink); flex: none; }

  .front-title-1 { left: 82px; top: 533px; font-size: 108px; letter-spacing: -1px; }
  .front-title-2 { left: 84px; top: 630px; font-size: 50px; letter-spacing: -0.5px; }
  .front-title-3 { left: 82px; top: 683px; font-size: 88px; }

  .call-band { position: absolute; left: 223px; top: 829px; width: 215px; height: 35px; background: var(--teal); border-radius: 10px 0 0 10px; color: #fff; font-family: "Roboto Condensed", sans-serif; font-weight: 700; font-size: 32px; line-height: 35px; padding-left: 7px; }
  .phone { position: absolute; left: 227px; top: 870px; font-family: "Roboto Condensed", sans-serif; font-weight: 700; font-size: 40px; line-height: 1; color: var(--grey-heading); letter-spacing: -1.5px; white-space: nowrap; }
  .address { position: absolute; left: 227px; top: 917px; font-family: "Roboto Condensed", sans-serif; font-weight: 700; font-size: 22px; line-height: 1.2; color: var(--grey-heading); white-space: nowrap; }

  /* back */
  .back-title-1 { left: 34px; top: 337px; font-size: 58px; }
  .back-title-2 { left: 34px; top: 390px; font-size: 27px; }
  .back-title-3 { left: 33px; top: 418px; font-size: 48px; }
  .about { position: absolute; left: 33px; top: 470px; width: 363px; font-size: 13.3px; line-height: 24px; color: var(--ink); text-align: justify; hyphens: auto; }
  .about p + p { margin-top: 24px; }

  .service-band { position: absolute; left: 197px; top: 822px; width: 241px; height: 33px; background: var(--teal); border-radius: 10px 0 0 10px; color: #fff; font-family: "Roboto Condensed", sans-serif; font-weight: 700; font-size: 30px; line-height: 33px; padding-left: 6px; }
  .service-list { position: absolute; left: 201px; top: 862px; list-style: none; font-family: "Roboto Condensed", sans-serif; font-size: 18px; line-height: 24.5px; color: var(--grey-heading); }
  .service-list li::before { content: ""; display: inline-block; width: 4px; height: 4px; background: var(--grey-heading); margin-right: 3px; vertical-align: 9px; }
  .web { position: absolute; left: 199px; top: 950px; font-size: 11px; letter-spacing: 1.8px; color: var(--teal); white-space: nowrap; }
</style>
</head>
<body>

<section class="card card--front">
  <svg class="card__art" viewBox="0 0 438 985" width="438" height="985">
    <defs>
      <linearGradient id="studioRoom" x1="0" y1="0" x2="1" y2="1">
        <stop offset="0" stop-color="#3b8c92"/>
        <stop offset="1" stop-color="#1f5f66"/>
      </linearGradient>
      <radialGradient id="babyScan" cx="0.45" cy="0.45" r="0.6">
        <stop offset="0" stop-color="var(--baby-light)"/>
        <stop offset="1" stop-color="var(--baby-dark)"/>
      </radialGradient>
    </defs>
    <rect role="img" aria-label="Ultrasound studio room with scan monitors, chair and exam bed" x="0" y="0" width="438" height="520" fill="url(#studioRoom)"/>
    <path d="M0,489 C50,421 110,406 170,409 C230,411 250,321 300,291 L438,249 L438,985 L0,985Z" fill="var(--teal)"/>
    <path d="M0,498 C50,430 110,415 170,418 C230,420 250,330 300,300 L438,258 L438,985 L0,985Z" fill="var(--paper)"/>
    <circle cx="342" cy="287" r="72" fill="var(--paper)" stroke="var(--teal)" stroke-width="3"/>
    <g stroke="var(--teal)" stroke-width="1.5">
      <circle role="img" aria-label="4D ultrasound image of a baby's face" cx="82" cy="855" r="31" fill="url(#babyScan)"/>
      <circle role="img" aria-label="4D ultrasound image of a baby in the womb" cx="163" cy="855" r="31" fill="url(#babyScan)"/>
      <circle role="img" aria-label="4D ultrasound image of a baby with hand to mouth" cx="82" cy="931" r="31" fill="url(#babyScan)"/>
      <circle role="img" aria-label="4D ultrasound image of a sleeping baby" cx="163" cy="931" r="31" fill="url(#babyScan)"/>
    </g>
  </svg>

  <div class="brand-name">4D Tiny Glimpse of Pace</div>
  <div class="partner">
    <span class="partner__name">Little<br>Heartbeat Buddy</span>
    <span class="partner__dot"></span>
  </div>

  <h1 class="heading front-title-1">4D/HD</h1>
  <div class="heading front-title-2">ULTRASOUND</div>
  <div class="heading front-title-3">STUDIO</div>

  <div class="call-band">CALL US</div>
  <div class="phone">8505550147</div>
  <div class="address">2716 -B HWY 38 Pace<br>FL 32590</div>
</section>

<section class="card card--back">
  <svg class="card__art" viewBox="0 0 438 985" width="438" height="985">
    <defs>
      <linearGradient id="staffPhoto" x1="0" y1="0" x2="1" y2="1">
        <stop offset="0" stop-color="#3a8a90"/>
        <stop offset="1" stop-color="#1d5a61"/>
      </linearGradient>
      <radialGradient id="babyScanBack" cx="0.5" cy="0.45" r="0.6">
        <stop offset="0" stop-color="var(--baby-light)"/>
        <stop offset="1" stop-color="var(--baby-dark)"/>
      </radialGradient>
    </defs>
    <rect role="img" aria-label="Two smiling studio staff members holding a gender reveal sign" x="0" y="0" width="438" height="500" fill="url(#staffPhoto)"/>
    <path d="M0,253 C80,241 160,241 200,291 C240,351 260,411 320,416 C380,421 420,461 438,484 L438,985 L0,985Z" fill="var(--teal)"/>
    <path d="M0,262 C80,250 160,250 200,300 C240,360 260,420 320,425 C380,430 420,470 438,493 L438,985 L0,985Z" fill="var(--paper)"/>
    <circle role="img" aria-label="4D ultrasound image of a baby in the womb" cx="99" cy="895" r="58" fill="url(#babyScanBack)" stroke="var(--teal)" stroke-width="3"/>
  </svg>

  <h2 class="heading back-title-1">4D/HD</h2>
  <div class="heading back-title-2">ULTRASOUND</div>
  <div class="heading back-title-3">STUDIO</div>

  <div class="about">
    <p>We are the premier 4D/HD Ultrasound studio in Pensacola/Pace as well as the greater panhandle area. We are a 4D/HD Ultrasound Studio in Pace, Florida, just a few minutes north of Pensacola. We offer 4D/HD imagining an early gender determination, 8 weeks by blood test and 14 weeks by ultrasound. We utilize the latest in 4D/HD technology to render beautiful images and memories that will last a lifetime.</p>
    <p>At 4D Tiny Glimpse of Pace, we give a whole new meaning to ultrasounds. We utilize the most up-to-date 4D/HD ultrasound imaging, so we can provide clear, amazing images of your unborn baby to life. Will she have your nose or her Daddy's smile? Book your appointment today for an unforgettable experience. We also offer heartbeat animals.</p>
  </div>

  <div class="service-band">OUR SERVICE</div>
  <ul class="service-list">
    <li>GENDER DETERMINATION</li>
    <li>ULTRASOUND</li>
    <li>BLOOD TEST</li>
  </ul>
  <div class="web">WWW.4DTINYGLIMPSE.EXAMPLE</div>
</section>

</body>
</html>
```